Website/Logo redesign: PlayfieldHub.com

We need a web design for a sports social network.
We have already built the web-site but are unhappy with the current design.
We like colours that evoke outdoors, eg sky blue and grass green.
Please see how it currently looks:
http://www.playfieldhub.example/6ce7bfd2fe66ba012a2a5e5217e2d776/
We are happy for everything to change, including logo, icons etc or for you to keep anything you think will work with your new design.
Updates
Project Deadline Extended
Reason: We have not yet found the design we are happy with so will be providing more feedback and extending the deadine.
We have increased the budget and also agreed to pay a second place award.
I will be giving existing and any new designs feedback daily.
Target Market(s)
Our target audience are mainly young sports players, but also older ones too.
Industry/Entity Type
Social
Look and feel
Each slider illustrates characteristics of the customer's brand and the style your logo design should communicate.

```html
<!DOCTYPE html>
<html lang="en">
<head>
<meta charset="utf-8">
<title>PlayfieldHub – Dashboard</title>
<link href="https://fonts.googleapis.com/css2?family=Ubuntu:wght@400;500&family=Open+Sans:wght@400;600&display=swap" rel="stylesheet">
<style>
:root{
  --grass:#8db224;
  --grass-dark:#6f9115;
  --grass-text:#6f8f0c;
  --sky:#2a67a8;
  --sky-btn:#2389c9;
  --ink:#333;
  --muted:#8a8a8a;
  --line:#d9d9d9;
  --panel:#f4f4f4;
  --bar-top:#f7f7f7;
  --bar-bot:#e6e6e6;
  --red:#e0382c;
  --orange:#d79b1d;
  --stat-blue:#3b7ea3;
}
*{box-sizing:border-box;margin:0;padding:0}
html,body{width:1200px;height:1004px;overflow:hidden;background:#fff}
body{font-family:"Open Sans",Arial,sans-serif;color:var(--ink)}
.stage{position:absolute;left:0;top:0;width:1100px;height:904px;transform-origin:0 0;transform:scale(1.0909,1.1106)}
.abs{position:absolute}
.ub{font-family:"Ubuntu","Open Sans",sans-serif}

/* header */
.topbar{left:0;top:0;width:1100px;height:72px;background:linear-gradient(#97bc2a,#86aa1d)}
.brand{left:38px;top:0;width:232px;height:72px;background:linear-gradient(#a3c638,#8eb224);border-bottom:4px solid #6e8c18;border-radius:0 0 3px 3px;display:flex;align-items:center;padding-left:16px;gap:10px;color:#fff;font-size:19px}
.brand-dot{width:14px;height:14px;border-radius:50%;background:#fff}
.nav-item{top:0;height:72px;border-left:1px solid #a9cb48;display:flex;flex-direction:column;align-items:center;justify-content:flex-end;padding-bottom:12px;color:#fff;font-size:14px}
.nav-item.active{background:#7b9b15}
.nav-item svg{margin-bottom:7px}
.signout{left:993px;top:80px;font-size:13px;color:var(--grass-dark)}

/* columns */
.col{top:105px;height:798px;border:1px solid var(--line)}
.col-left{left:43px;width:220px;background:var(--panel)}
.col-mid{left:275px;width:537px;background:#fff}
.col-right{left:825px;width:220px;background:#f7f7f7}

.bar{height:29px;background:linear-gradient(var(--bar-top),var(--bar-bot));border-top:1px solid #e2e2e2;border-bottom:1px solid #dcdcdc;display:flex;align-items:center;font-size:12.5px;color:#444;font-family:"Ubuntu",sans-serif}
.go{width:14px;height:14px;border:1.5px solid #444;border-radius:50%;display:inline-block;position:relative}
.go::after{content:"";position:absolute;left:4px;top:2.5px;border-left:5px solid #444;border-top:3px solid transparent;border-bottom:3px solid transparent}
.go.down::after{left:2.5px;top:4px;border-top:5px solid #444;border-left:3px solid transparent;border-right:3px solid transparent;border-bottom:0}

.photo{border:3px solid #eee;background:linear-gradient(#b59a7a,#6c8f5c)}
.photo.alt{background:linear-gradient(#c78a5c,#b63a2c)}
.photo.gent{background:linear-gradient(#c9bfb5,#5a6f96)}

.team{font-size:11px}
.team .home{color:var(--grass-text)}
.team .vs{color:#777;margin:0 4px}
.team .away{color:var(--sky)}
.when{font-size:11px;color:#333}
.small{font-size:11px;color:#555}
.vote{font-size:12px;color:#444;display:flex;align-items:center;gap:4px}
.muted{color:var(--muted)}
.dash{height:0;border-top:1px dashed #c9c9c9}
.round-ic{width:26px;height:26px;border-radius:50%;background:#e2e2e2;display:flex;align-items:center;justify-content:center}

.list-row{left:0;width:218px;height:31px;border-bottom:1px solid #ddd;background:linear-gradient(#f6f6f6,#ececec);font-size:11px;display:flex;align-items:center;padding-left:13px}
.league-row{left:13px;width:193px;display:flex;font-size:11px;color:#333}
</style>
</head>
<body>
<svg width="0" height="0" style="position:absolute">
  <defs>
    <symbol id="thumb-up" viewBox="0 0 20 18"><rect x="1" y="8" width="5" height="9" fill="#8db224"/><path d="M7 17V8l4-6c1.5 0 2 1 1.6 2.5L12 7h5c1 0 1.6.8 1.4 1.8l-1.2 6.5c-.2 1-1 1.7-2 1.7z" fill="#fff" stroke="#8db224" stroke-width="1.4"/></symbol>
    <symbol id="thumb-down" viewBox="0 0 20 18"><rect x="14" y="1" width="5" height="9" fill="#e0382c"/><path d="M13 1v9l-4 6c-1.5 0-2-1-1.6-2.5L8 11H3c-1 0-1.6-.8-1.4-1.8L2.8 2.7C3 1.7 3.8 1 4.8 1z" fill="#fff" stroke="#e0382c" stroke-width="1.4"/></symbol>
    <symbol id="shield" viewBox="0 0 22 22"><circle cx="11" cy="11" r="11" fill="#dcdcdc"/><path d="M6 7c2 0 3.5-.6 5-1.5C12.5 6.4 14 7 16 7v4c0 3-2.5 4.8-5 5.8C8.5 15.8 6 14 6 11z" fill="#7a7a7a"/></symbol>
    <symbol id="shield-blue" viewBox="0 0 22 22"><circle cx="11" cy="11" r="11" fill="#dcdcdc"/><path d="M6 7c2 0 3.5-.6 5-1.5C12.5 6.4 14 7 16 7v4c0 3-2.5 4.8-5 5.8C8.5 15.8 6 14 6 11z" fill="#4f86c6"/></symbol>
    <symbol id="ball" viewBox="0 0 30 30"><circle cx="15" cy="15" r="15" fill="#e4e4e4"/><circle cx="15" cy="15" r="10" fill="#fff" stroke="#222" stroke-width="1.4"/><path d="M15 10l4 3-1.5 4.5h-5L11 13z" fill="#222"/><path d="M15 5v5M19 13l5-2M17.5 17.5l3 4M12.5 17.5l-3 4M11 13l-5-2" stroke="#222" stroke-width="1.2"/></symbol>
    <symbol id="chat" viewBox="0 0 26 26"><circle cx="13" cy="13" r="13" fill="#e2e2e2"/><path d="M7 8h10v7h-5l-3 3v-3H7z" fill="#8a8a8a"/><path d="M18 10h2v7h-2v2l-2-2h-3" fill="none" stroke="#8a8a8a" stroke-width="1.3"/></symbol>
    <symbol id="note" viewBox="0 0 26 26"><circle cx="13" cy="13" r="13" fill="#e2e2e2"/><rect x="8" y="7" width="10" height="12" rx="1" fill="#8a8a8a"/><path d="M10 10h6M10 13h6M10 16h6" stroke="#e2e2e2" stroke-width="1"/></symbol>
  </defs>
</svg>

<div class="stage">
  <!-- header -->
  <div class="abs topbar"></div>
  <div class="abs brand ub"><span class="brand-dot"></span>PlayfieldHub</div>

  <div class="abs nav-item active ub" style="left:320px;width:89px">
    <svg width="26" height="28" viewBox="0 0 26 28"><ellipse cx="13" cy="12" rx="12" ry="10" fill="#f2f2f2"/><path d="M8 20l-2 6 7-5" fill="#f2f2f2"/><text x="13" y="17" text-anchor="middle" font-size="13" font-weight="bold" fill="#888">?</text></svg>Headlines</div>
  <div class="abs nav-item ub" style="left:409px;width:95px">
    <svg width="28" height="26" viewBox="0 0 28 26"><rect x="1" y="1" width="26" height="18" fill="#2f6b2f" stroke="#8a5a2b" stroke-width="2"/><path d="M7 24l4-5M21 24l-4-5" stroke="#8a5a2b" stroke-width="2"/></svg>My School</div>
  <div class="abs nav-item ub" style="left:504px;width:88px">
    <svg width="30" height="24" viewBox="0 0 30 24"><path d="M2 22a13 13 0 0 1 26 0z" fill="#e8b21f"/><path d="M15 22L15 9a13 13 0 0 1 13 13z" fill="#d8452e"/><path d="M15 22L6 12a13 13 0 0 1 9-3z" fill="#4f9ad4"/></svg>My Stats</div>
  <div class="abs nav-item ub" style="left:592px;width:94px">
    <svg width="22" height="28" viewBox="0 0 22 28"><path d="M4 2h14v8a7 7 0 0 1-14 0z" fill="#f1c21a"/><rect x="9" y="16" width="4" height="6" fill="#f1c21a"/><rect x="5" y="22" width="12" height="4" fill="#d9a514"/></svg>Challengers</div>
  <div class="abs nav-item ub" style="left:686px;width:88px">
    <svg width="28" height="26" viewBox="0 0 28 26"><rect x="1" y="2" width="26" height="23" fill="#f4f4f4" stroke="#bbb"/><rect x="1" y="2" width="26" height="5" fill="#d9d9d9"/><path d="M5 11h18M5 15h18M5 19h18M9 9v14M14 9v14M19 9v14" stroke="#c7c7c7" stroke-width="1"/></svg>Fixtures</div>
  <div class="abs nav-item ub" style="left:774px;width:90px">
    <svg width="36" height="26" viewBox="0 0 36 26"><circle cx="9" cy="8" r="4" fill="#e2c6a4"/><circle cx="27" cy="8" r="4" fill="#e2c6a4"/><circle cx="18" cy="7" r="5" fill="#e2c6a4"/><path d="M2 22a7 7 0 0 1 14 0zM20 22a7 7 0 0 1 14 0z" fill="#d2a77c"/><path d="M10 24a8 8 0 0 1 16 0z" fill="#7db13b"/></svg>Teams</div>
  <div class="abs nav-item ub" style="left:864px;width:91px">
    <svg width="26" height="28" viewBox="0 0 26 28"><path d="M2 4c4 0 8-1 11-3 3 2 7 3 11 3v9c0 7-6 11-11 13C8 24 2 20 2 13z" fill="#2f74b8" stroke="#1a4f85" stroke-width="1.5"/></svg>Leagues</div>
  <div class="abs nav-item ub" style="left:955px;width:85px;border-right:1px solid #a9cb48">
    <svg width="28" height="28" viewBox="0 0 28 28"><path d="M4 24L18 10" stroke="#dcdcdc" stroke-width="4" stroke-linecap="round"/><path d="M24 24L10 10" stroke="#9a9a9a" stroke-width="4" stroke-linecap="round"/><circle cx="20" cy="7" r="5" fill="none" stroke="#dcdcdc" stroke-width="3"/></svg>Tools</div>

  <div class="abs signout ub">Signout</div>

  <!-- left column -->
  <div class="abs col col-left">
    <div class="abs photo" style="left:10px;top:15px;width:64px;height:61px" role="img" aria-label="Profile photo of the player"></div>
    <div class="abs" style="left:100px;top:14px;width:85px;text-align:center;font-size:12px">Sam Carver</div>
    <div class="abs" style="left:84px;top:38px;width:124px;display:flex;justify-content:space-between;font-size:8px;color:#fff;text-align:center">
      <div style="width:40px"><div style="width:16px;height:16px;border-radius:50%;background:var(--stat-blue);margin:0 auto;line-height:16px">24</div><div class="muted" style="margin-top:9px;font-size:9px">Played</div></div>
      <div style="width:40px"><div style="width:16px;height:16px;border-radius:50%;background:var(--grass);margin:0 auto;line-height:16px">3</div><div class="muted" style="margin-top:9px;font-size:9px">Teams</div></div>
      <div style="width:40px"><div style="width:16px;height:16px;border-radius:50%;background:var(--orange);margin:0 auto;line-height:16px">7</div><div class="muted" style="margin-top:9px;font-size:9px">Awards</div></div>
    </div>
    <div class="abs" style="left:0;top:116px;width:218px;height:8px;background:radial-gradient(ellipse at top,#d8d8d8,transparent 70%)"></div>
    <div class="abs ub" style="left:11px;top:152px;width:196px;height:32px;border-radius:3px;background:linear-gradient(#45a9e0,#1d78b8);color:#fff;font-size:13.5px;display:flex;align-items:center;padding-left:10px;gap:12px">
      <span style="width:16px;height:16px;border-radius:50%;background:#1a5d96;display:flex;align-items:center;justify-content:center;font-size:13px;line-height:1">+</span>CREATE NEW FIXTURES</div>

    <div class="abs bar" style="left:0;top:227px;width:218px;justify-content:flex-end;padding-right:13px;gap:6px;font-size:11px">All Teams <span class="go"></span></div>
    <div class="abs list-row" style="top:257px">U15 Football Team B</div>
    <div class="abs list-row" style="top:288px">Galatians House</div>
    <div class="abs list-row" style="top:319px">U15 Rugby Team A</div>

    <div class="abs ub" style="left:0;top:368px;width:218px;text-align:center;font-size:13.5px">Quotes of the day</div>
    <div class="abs" style="left:0;top:389px;width:218px;height:8px;background:radial-gradient(ellipse at top,#d8d8d8,transparent 70%)"></div>
    <div class="abs" style="left:18px;top:408px;width:189px;font-size:11.5px;line-height:20px;color:#777;text-align:justify">Champions aren’t made in the gyms.Champions are made from Something they have deep inside them - a desire, a dream, a vision</div>
    <div class="abs" style="left:101px;top:503px;display:flex;align-items:center;gap:7px;font-size:12px;font-family:Ubuntu,sans-serif"><span class="go"></span>Marcus Bell</div>
  </div>

  <!-- middle column -->
  <div class="abs col col-mid">
    <div class="abs bar" style="left:0;top:14px;width:535px;padding:0 15px;justify-content:space-between">Next Fixture <span class="go"></span></div>
    <svg class="abs" style="left:17px;top:57px" width="30" height="30"><use href="#ball"/></svg>
    <svg class="abs" style="left:64px;top:61px" width="20" height="20"><use href="#shield"/></svg>
    <div class="abs team" style="left:103px;top:61px"><span class="home">U15 Football Team</span><span class="vs">Vs</span><span class="away">Colossians House</span></div>
    <div class="abs when" style="left:103px;top:85px">Sunday 29th &nbsp;July &nbsp;&nbsp;&nbsp;1PM</div>
    <div class="abs vote" style="left:385px;top:104px">I’m in <svg width="20" height="18"><use href="#thumb-up"/></svg>&nbsp;&nbsp;&nbsp;I’m out <svg width="20" height="18"><use href="#thumb-down"/></svg></div>
    <div class="abs dash" style="left:2px;top:151px;width:533px"></div>
    <svg class="abs" style="left:384px;top:139px" width="26" height="26"><use href="#chat"/></svg>
    <svg class="abs" style="left:428px;top:139px" width="26" height="26"><use href="#note"/></svg>

    <div class="abs photo gent" style="left:15px;top:179px;width:49px;height:48px" role="img" aria-label="Coach profile photo"></div>
    <div class="abs" style="left:75px;top:176px;font-size:12px;color:#444">Mr Pembridge</div>
    <div class="abs small muted" style="left:74px;top:195px;line-height:18px">Dont,t be late minibus wil be leaving at 11:30 AM on the dot,<br>anybody late will miss it !</div>
    <div class="abs small" style="right:18px;top:237px">2m ago</div>

    <div class="abs photo alt" style="left:15px;top:250px;width:49px;height:48px" role="img" aria-label="Player profile photo"></div>
    <div class="abs" style="left:75px;top:247px;font-size:12px;color:#444">Mr Pembridge</div>
    <div class="abs small muted" style="left:74px;top:266px;line-height:18px">Dont,t be late minibus wil be leaving at 11:30 AM on the dot,<br>anybody late will miss it !</div>
    <div class="abs small" style="right:18px;top:308px">2m ago</div>

    <div class="abs" style="left:140px;top:325px;width:283px;height:27px;border:1px solid #ccc;border-radius:14px;display:flex;overflow:hidden">
      <div style="flex:1;font-size:10px;color:#bbb;padding:6px 0 0 14px">Leave your Comments Here</div>
      <div style="width:66px;background:linear-gradient(#8aa92a,#6f8d17);color:#fff;font-size:11px;display:flex;align-items:center;justify-content:center">SUBMIT</div>
    </div>

    <div class="abs bar" style="left:0;top:374px;width:535px;padding:0 15px;justify-content:space-between">Last Result <span class="go"></span></div>
    <svg class="abs" style="left:15px;top:417px" width="30" height="30"><use href="#ball"/></svg>
    <svg class="abs" style="left:62px;top:421px" width="20" height="20"><use href="#shield"/></svg>
    <div class="abs team" style="left:101px;top:424px"><span class="home">Ashford Vale</span><span class="vs">Vs</span><span class="away">Kingsmere Park U15</span></div>
    <div class="abs when" style="left:101px;top:448px">Friday 27th &nbsp;July &nbsp;&nbsp;&nbsp;1PM</div>
    <div class="abs" style="left:102px;top:470px;display:flex;align-items:center;gap:8px;font-size:12px">
      <span style="width:25px;height:24px;border:1px solid #ccc;border-radius:3px;background:#eee;text-align:center;line-height:22px">2</span>:<span style="width:25px;height:24px;border:1px solid #ccc;border-radius:3px;background:#eee;text-align:center;line-height:22px">1</span></div>
    <div class="abs dash" style="left:2px;top:517px;width:533px"></div>
    <svg class="abs" style="left:384px;top:505px" width="26" height="26"><use href="#chat"/></svg>
    <svg class="abs" style="left:428px;top:505px" width="26" height="26"><use href="#note"/></svg>

    <div class="abs bar" style="left:0;top:546px;width:535px;padding:0 15px 0 55px;justify-content:space-between">News Feed <span class="go"></span></div>
    <div class="abs photo gent" style="left:14px;top:598px;width:51px;height:48px" role="img" aria-label="Coach profile photo"></div>
    <svg class="abs" style="left:95px;top:599px" width="22" height="22"><use href="#shield"/></svg>
    <div class="abs team" style="left:134px;top:600px"><span class="home">U15 Football Team</span><span class="vs">Vs</span><span class="away">Colossians House</span></div>
    <div class="abs when" style="left:134px;top:624px">Sunday 29th &nbsp;July &nbsp;&nbsp;&nbsp;1PM</div>
    <svg class="abs" style="left:501px;top:606px" width="16" height="15" viewBox="0 0 16 15"><rect x="1" y="1" width="14" height="13" fill="#fff" stroke="#888"/><rect x="1" y="1" width="14" height="3" fill="#888"/><path d="M3 7h10M3 10h10" stroke="#aaa"/></svg>
    <div class="abs vote" style="left:222px;top:654px"><svg width="20" height="18"><use href="#thumb-up"/></svg>I’m in &nbsp;&nbsp;&nbsp;&nbsp;&nbsp;<svg width="20" height="18"><use href="#thumb-down"/></svg>I’m out</div>
    <div class="abs small" style="right:18px;top:655px">1h ago</div>

    <div class="abs photo alt" style="left:14px;top:700px;width:51px;height:49px" role="img" aria-label="Player profile photo"></div>
    <svg class="abs" style="left:93px;top:707px" width="22" height="22"><use href="#shield-blue"/></svg>
    <div class="abs team" style="left:134px;top:706px"><span class="home">U15 Football Team</span><span class="vs">Vs</span><span class="away">Colossians House</span></div>
    <div class="abs when" style="left:134px;top:730px">Sunday 29th &nbsp;July &nbsp;&nbsp;&nbsp;1PM</div>
    <div class="abs vote" style="left:222px;top:757px"><svg width="20" height="18"><use href="#thumb-up"/></svg>I’m in &nbsp;&nbsp;&nbsp;&nbsp;&nbsp;<svg width="20" height="18"><use href="#thumb-down"/></svg>I’m out</div>
    <div class="abs small" style="right:18px;top:758px">6h ago</div>
  </div>

  <!-- right column -->
  <div class="abs col col-right">
    <div class="abs bar" style="left:0;top:21px;width:218px;padding:0 13px;justify-content:space-between">Upcoming Events <span class="go"></span></div>
    <div class="abs" style="left:22px;top:83px;width:1px;height:167px;background:#aaa"></div>
    <svg class="abs" style="left:12px;top:72px" width="22" height="22"><use href="#shield"/></svg>
    <svg class="abs" style="left:12px;top:115px" width="22" height="22"><use href="#shield-blue"/></svg>
    <div class="abs team" style="left:57px;top:73px;line-height:18px"><span class="home">U15 Football Team</span><span class="vs">Vs</span><br><span class="away">Colossians House</span></div>
    <div class="abs when" style="left:57px;top:109px">29th &nbsp;July</div>
    <div class="abs vote" style="left:150px;top:139px;font-size:11px">I’m in &nbsp;<svg width="18" height="17"><use href="#thumb-up"/></svg></div>
    <div class="abs" style="left:30px;top:175px;width:180px;height:1px;background:linear-gradient(90deg,transparent,#ccc,transparent)"></div>
    <svg class="abs" style="left:12px;top:196px" width="22" height="22"><use href="#shield"/></svg>
    <svg class="abs" style="left:12px;top:239px" width="22" height="22"><use href="#shield-blue"/></svg>
    <div class="abs team" style="left:57px;top:198px;line-height:18px"><span class="home">U15 Football Team</span><span class="vs">Vs</span><br><span class="away">Romans House</span></div>
    <div class="abs when" style="left:57px;top:234px">6th &nbsp;July</div>
    <div class="abs vote" style="left:150px;top:269px;font-size:11px">I’m in &nbsp;<svg width="18" height="17"><use href="#thumb-up"/></svg></div>

    <div class="abs bar" style="left:0;top:310px;width:218px;padding:0 13px;justify-content:space-between">League Table <span class="go"></span></div>
    <div class="abs bar" style="left:0;top:341px;width:218px;padding:0 13px;justify-content:space-between;font-size:11px;background:linear-gradient(#fafafa,#ededed)">Ashford Inter House Football <span class="go down"></span></div>

    <div class="abs league-row" style="top:392px"><span style="width:20px">1</span><span style="flex:1">Colossians</span><span style="width:32px">12</span><span>36</span></div>
    <div class="abs dash" style="left:9px;top:416px;width:204px;border-color:#888"></div>
    <div class="abs league-row" style="top:429px"><span style="width:20px">1</span><span style="flex:1">Phillippians</span><span style="width:32px">12</span><span>36</span></div>
    <div class="abs dash" style="left:9px;top:457px;width:204px;border-color:#888"></div>
    <div class="abs league-row" style="top:472px"><span style="width:20px">1</span><span style="flex:1;color:var(--sky)">Galatians</span><span style="width:32px">12</span><span>36</span></div>
    <div class="abs dash" style="left:9px;top:500px;width:204px;border-color:#888"></div>
    <div class="abs league-row" style="top:514px"><span style="width:20px">1</span><span style="flex:1">Romans</span><span style="width:32px">12</span><span>36</span></div>
    <div class="abs dash" style="left:9px;top:541px;width:204px;border-color:#888"></div>
    <div class="abs league-row" style="top:553px"><span style="width:20px">1</span><span style="flex:1">Corinthians</span><span style="width:32px">12</span><span>36</span></div>
  </div>
</div>
</body>
</html>
```